Modern, pro female massage business needs business card design

We are a boutique, pro women's sports and remedial massage studio based in Singapore - we have a logo already (see attached image) and need to design a business card that reflects an elegant, modern and feminine feel using this logo.

We are focussed on a very local market and need to give a professional yet warm feeling.

Details for the card include (layout of your choice):

Tamsin Vale
Call, SMS or WhatsApp: 9183 6027
Email: bluefennel@mailbox-example.com
Address: The Harbourview on Talbot
72 Talbot Road, Westmere, Singapore

To incorporate the QRAB logo (www.qrabglobal.co.uk) would be appreciated - see attached file.

Industry/Entity Type

Massage

Requirements
Nice to have
• We like the idea of using an embossed style card. Solid colour on the reverse - embossed on the front; four colour printing is okay.
Should not have
• It should not be uber 'girly girl' if that makes any sense. The logo is already colourful

```html
<!DOCTYPE html>
<html lang="en">
<head>
<meta charset="utf-8">
<title>Tamsin Vale – Business Card</title>
<link href="https://fonts.googleapis.com/css2?family=Didact+Gothic&display=swap" rel="stylesheet">
<style>
  :root {
    --page: #ffffff;
    --board: #2a2a2b;
    --board-light: #3a3a3b;
    --teal: #0e8b8e;
    --teal-deep: #0a6f72;
    --ink: #f2f7f7;
    --icon: #b9d5d8;
    --brand-blue: #3e7fc6;
  }
  * { box-sizing: border-box; margin: 0; padding: 0; }
  html, body {
    width: 1200px; height: 1000px; overflow: hidden;
    background: var(--page);
  }
  .card-front {
    position: absolute; left: 38px; top: 163px;
    width: 1125px; height: 675px;
    background: var(--board);
    overflow: hidden;
    font-family: "Didact Gothic", sans-serif;
  }
  .board-texture {
    position: absolute; inset: 0;
    background: radial-gradient(ellipse at 30% 40%, var(--board-light), var(--board) 70%);
  }
  .peel { position: absolute; left: 0; top: 0; }
  .brand {
    position: absolute; left: 37px; top: 40px;
    width: 80px; display: flex; flex-direction: column; align-items: center; gap: 6px;
  }
  .brand-dot {
    width: 70px; height: 70px; border-radius: 50%;
    background: var(--brand-blue);
  }
  .brand-name {
    color: var(--ink); font-size: 26px; letter-spacing: 4px;
  }
  .contact-row {
    position: absolute; left: 366px;
    display: flex; align-items: flex-start; gap: 12px;
    color: var(--ink);
  }
  .contact-row svg { flex: none; fill: var(--icon); }
  .contact-name { top: 172px; font-size: 33px; }
  .contact-address { top: 254px; font-size: 28px; line-height: 41px; }
  .contact-phone { top: 362px; font-size: 30px; }
  .contact-email { top: 443px; font-size: 28px; }
</style>
</head>
<body>
  <div class="card-front">
    <div class="board-texture"></div>

    <svg class="peel" width="1125" height="675" viewBox="0 0 1125 675">
      <defs>
        <linearGradient id="curlShade" x1="0" y1="0" x2="1" y2="0.3">
          <stop offset="0" stop-color="#2c2c2d"/>
          <stop offset="0.7" stop-color="#3a3a3b"/>
          <stop offset="1" stop-color="#1a1a1a"/>
        </linearGradient>
        <linearGradient id="tealEdge" x1="0" y1="0" x2="1" y2="0">
          <stop offset="0" stop-color="#063d40"/>
          <stop offset="0.25" stop-color="#0a6f72"/>
          <stop offset="0.5" stop-color="#0e8b8e"/>
        </linearGradient>
        <filter id="cardShadow" x="-5%" y="-5%" width="110%" height="115%">
          <feDropShadow dx="0" dy="6" stdDeviation="6" flood-color="#000" flood-opacity="0.55"/>
        </filter>
      </defs>
      <!-- teal card with peeled left edge -->
      <path filter="url(#cardShadow)" fill="var(--teal)"
            d="M244 159 H994 V509 H336 C300 450 275 380 244 340 Z"/>
      <path fill="url(#tealEdge)" opacity="0.8"
            d="M244 300 C275 380 300 450 336 509 H420 C370 460 320 380 244 300 Z"/>
      <!-- lifted curl -->
      <path fill="url(#curlShade)"
            d="M190 300 C230 330 270 400 300 460 C315 490 330 505 345 520 C300 510 240 470 200 420 C180 390 175 330 190 300 Z"/>
    </svg>

    <div class="brand">
      <div class="brand-dot"></div>
      <div class="brand-name">QRAB</div>
    </div>

    <div class="contact-row contact-name">
      <svg width="38" height="38" viewBox="0 0 38 38" aria-hidden="true">
        <circle cx="19" cy="12" r="10"/>
        <path d="M0 38 C0 26 8 22 19 22 C30 22 38 26 38 38 Z"/>
      </svg>
      <span>Tamsin Vale</span>
    </div>

    <div class="contact-row contact-address">
      <svg width="34" height="42" viewBox="0 0 34 42" aria-hidden="true" style="margin-top:2px">
        <path d="M17 0 C7 0 2 7 2 14 C2 24 17 42 17 42 C17 42 32 24 32 14 C32 7 27 0 17 0 Z M17 8 A6 6 0 1 1 17 20 A6 6 0 1 1 17 8 Z"/>
      </svg>
      <span>The Harbourview on Talbot<br>72 Talbot Road, Westmere, Singapore</span>
    </div>

    <div class="contact-row contact-phone">
      <svg width="34" height="34" viewBox="0 0 34 34" aria-hidden="true">
        <path d="M7 1 L12 9 L8 13 C10 18 15 23 20 25 L24 21 L33 26 L29 33 C15 32 2 19 1 5 Z"/>
      </svg>
      <span>9183 6027</span>
    </div>

    <div class="contact-row contact-email">
      <svg width="34" height="26" viewBox="0 0 34 26" aria-hidden="true" style="margin-top:6px">
        <path d="M0 0 H34 V26 H0 Z M3 3 V23 H31 V3 L17 15 Z M5 3 L17 13 L29 3 Z" fill-rule="evenodd"/>
      </svg>
      <span>bluefennel@mailbox-example.com</span>
    </div>
  </div>
</body>
</html>
```